Label designs for three different cider varieties

The Larkmoor Perry Works is a family run business. We have been making cider within the family as a hobby for over 100 years and we have recently decided to start to try to sell the cider. Therefore this project is to create a logo and three product labels for three different varieties of cider. So we should end up with four files; one for the logo and one for each of the labels. The files need to be in an editable format for us so that we can add edit the batch numbers e.g. PNG file.
For the logo we would like to use the Pellow Family Shield since Pellow is our family name. We would like it adapted into a cider themed crest, for example with apples and trees. We are open to ideas about the logo but this is just our initial idea. Example of the original Pellow Family Shield can be seen in the link below:
http://www.vinshadeheraldry.net/arms/Pellow-England.jpg
The labels should be no bigger than 93mm in height and 213mm in length. Each label should be similar in style so it is clear the three different varieties of cider are from the same company. Each label must have the following information since this is a legal requirement:
- The logo you have created
- The Larkmoor Perry Works Ltd.
- 52 Mirefield Row, Taunton, Somerset, TA4 9QX
- Alcohol: 6% vol
- 500ml
- Allergens: Contains Sulphites for freshness
- There needs to be space on the label for batch numbers. This is four numbers e.g. 1701.
- Family craft cider makers using only premium apples from our own traditional Somerset orchard.
The names of the three cider varieties are:
- Larkmoor Heritage
- Larkmoor Amber
- Larkmoor Kingsbury
Our initial idea is that each variety would have its own colour associated with it; i.e. black themed label for Larkmoor Heritage, gold themed label for Larkmoor Amber and a red themed label for Larkmoor Kingsbury. The crest logo you have created would then be in the themed colour for that cider variety i.e. black, gold or red.
We would like the labels to reflect the following themes for our brand:
- High end premium brand
- Clean and simple design
- Modern
Overall we are very open to ideas and we do not want to constrain your creativity. All of the above is just our initial ideas but we would love to see what ideas you have. The only things that cannot change are what must be on the label since this is a legal requirement we have to meet.

```html
<!DOCTYPE html>
<html lang="en">
<head>
<meta charset="utf-8">
<title>The Larkmoor Perry Works – Cider Label Range</title>
<link rel="stylesheet" href="https://fonts.googleapis.com/css2?family=Bebas+Neue&family=Oswald:wght@400&family=Dancing+Script:wght@600&family=Open+Sans:wght@400&display=swap">
<style>
  :root {
    --page: #e7e7e8;
    --panel: #48494b;
    --gold: #c9a54a;
    --gold-light: #e2c57a;
    --white: #ffffff;
    --ink-soft: #d9d9d9;
    --heritage: #1e1e1f;
    --heritage-back: #252526;
    --kingsbury: #7c0b0e;
    --amber: #6a5a14;
    --neck: #1a1a1a;
  }
  * { box-sizing: border-box; margin: 0; padding: 0; }
  html, body { width: 1200px; height: 710px; overflow: hidden; }
  body {
    position: relative;
    background: var(--page);
    font-family: "Oswald", "Arial Narrow", sans-serif;
    color: var(--white);
  }

  /* Brand mark panel */
  .brand-panel {
    position: absolute; left: 0; top: 0; width: 168px; height: 710px;
    background: var(--panel);
    display: flex; flex-direction: column; justify-content: space-around; align-items: center;
    padding: 40px 0;
  }
  .mark {
    display: flex; align-items: center; gap: 8px;
    font-family: "Oswald", sans-serif; font-weight: 400;
    font-size: 17px; line-height: 1.15; text-transform: uppercase; letter-spacing: 0.5px;
    width: 128px;
  }
  .mark-dot { flex: none; width: 14px; height: 14px; border-radius: 50%; background: currentColor; }
  .mark--gold { color: var(--gold); }
  .mark--white { color: var(--white); }

  /* Label range */
  .range { position: absolute; left: 200px; top: 0; width: 980px; height: 710px; }
  .variety { position: absolute; top: 0; width: 230px; height: 710px; }
  .variety:nth-child(1) { left: 0; }
  .variety:nth-child(2) { left: 250px; }
  .variety:nth-child(3) { left: 500px; }
  .variety:nth-child(4) { left: 750px; }

  .neck-label {
    position: absolute; left: 55px; top: 70px; width: 120px; height: 80px;
    background: var(--neck);
    border-top: 2px solid var(--gold); border-bottom: 2px solid var(--gold);
    display: flex; align-items: center; justify-content: center;
  }
  .neck-label .mark { font-size: 11px; width: 96px; gap: 6px; color: var(--gold); }
  .neck-label .mark-dot { width: 9px; height: 9px; }

  .body-label {
    position: absolute; left: 0; top: 200px; width: 230px; height: 300px;
    border-top: 2px solid var(--gold); border-bottom: 2px solid var(--gold);
    box-shadow: inset 0 0 0 4px rgba(0,0,0,0.15);
    overflow: hidden;
  }
  .body-label::before, .body-label::after {
    content: ""; position: absolute; left: 0; right: 0; height: 1px; background: var(--gold);
  }
  .body-label::before { top: 4px; }
  .body-label::after { bottom: 4px; }

  .label--heritage { background: var(--heritage); }
  .label--back { background: var(--heritage-back); }
  .label--kingsbury { background: radial-gradient(circle at 50% 40%, #951216, var(--kingsbury) 70%); }
  .label--amber { background: radial-gradient(circle at 50% 40%, #7f6c1b, var(--amber) 70%); }

  .fruit-art {
    position: absolute; left: 35px; top: 28px; width: 160px; height: 150px; border-radius: 50%;
    background: radial-gradient(circle, rgba(255,255,255,0.07), rgba(255,255,255,0) 70%);
  }

  .front-mark {
    position: absolute; top: 18px; left: 0; right: 0; display: flex; justify-content: center;
  }
  .front-mark .mark { width: 100px; font-size: 12px; color: var(--gold); gap: 6px; }
  .front-mark .mark-dot { width: 10px; height: 10px; }

  .variety-name {
    position: absolute; top: 112px; left: 0; right: 0; text-align: center;
    font-family: "Bebas Neue", "Oswald", sans-serif; font-size: 34px; line-height: 0.92;
    color: var(--white); letter-spacing: 0.5px;
  }
  .variety-style {
    position: absolute; top: 180px; left: 0; right: 0; text-align: center;
    font-family: "Dancing Script", cursive; font-size: 13px; color: var(--gold-light);
  }
  .style-rule {
    position: absolute; top: 202px; left: 20px; right: 20px; height: 1px;
    background: linear-gradient(90deg, transparent, var(--gold), transparent);
  }

  .info-row {
    position: absolute; left: 12px; right: 12px; top: 218px; height: 64px;
    display: flex; align-items: stretch;
    border-top: 1px solid rgba(201,165,74,0.4);
  }
  .info-figures {
    width: 46px; display: flex; flex-direction: column; justify-content: center; align-items: center;
    font-size: 8px; line-height: 1.2; text-align: center; border-right: 1px solid rgba(255,255,255,0.35);
  }
  .info-figures .volume { margin-top: 8px; padding-top: 6px; border-top: 1px solid rgba(255,255,255,0.35); }
  .info-pledge {
    flex: 1; padding: 6px 6px; font-size: 7.5px; line-height: 1.3; text-align: center;
    text-transform: uppercase; color: var(--ink-soft);
    display: flex; align-items: center; justify-content: center;
    border-right: 1px solid rgba(255,255,255,0.35);
  }
  .tree-art {
    width: 40px; margin: 10px 0 10px 6px;
    background: radial-gradient(circle at 50% 40%, rgba(255,255,255,0.55), rgba(255,255,255,0.1) 70%);
    border-radius: 4px;
  }

  /* Back label */
  .back-head { position: absolute; left: 12px; top: 20px; width: 150px; }
  .back-title {
    font-family: "Bebas Neue", "Oswald", sans-serif; font-size: 24px; line-height: 0.95; color: var(--ink-soft);
  }
  .back-address { margin-top: 4px; font-size: 5.5px; line-height: 1.35; text-transform: uppercase; color: var(--ink-soft); }
  .back-mark { position: absolute; right: 10px; top: 24px; }
  .back-mark .mark { width: 62px; font-size: 8px; gap: 4px; color: var(--gold); }
  .back-mark .mark-dot { width: 7px; height: 7px; }
  .label--back .info-row { top: 90px; height: 58px; border-top: none; }
  .batch {
    position: absolute; right: 12px; top: 142px; font-size: 6px; text-transform: uppercase; color: var(--ink-soft);
  }
  .allergens {
    position: absolute; left: 12px; right: 12px; top: 160px; text-align: center;
    font-size: 7.5px; text-transform: uppercase; letter-spacing: 0.3px; color: var(--white);
  }
  .story {
    position: absolute; left: 12px; right: 12px; top: 178px;
    font-family: "Open Sans", sans-serif; font-size: 5.6px; line-height: 1.45; color: var(--ink-soft);
  }
  .story p + p { margin-top: 5px; }
  .back-rule {
    position: absolute; bottom: 14px; left: 70px; right: 70px; height: 1px;
    background: linear-gradient(90deg, transparent, var(--gold), transparent);
  }
</style>
</head>
<body>

<aside class="brand-panel">
  <div class="mark mark--gold"><span class="mark-dot"></span><span>The Larkmoor Perry Works</span></div>
  <div class="mark mark--gold"><span class="mark-dot"></span><span>The Larkmoor Perry Works</span></div>
  <div class="mark mark--white"><span class="mark-dot"></span><span>The Larkmoor Perry Works</span></div>
</aside>

<main class="range">

  <section class="variety">
    <div class="neck-label"><div class="mark"><span class="mark-dot"></span><span>The Larkmoor Perry Works</span></div></div>
    <div class="body-label label--heritage">
      <div class="fruit-art" role="img" aria-label="Faint engraved apple illustration"></div>
      <div class="front-mark"><div class="mark"><span class="mark-dot"></span><span>The Larkmoor Perry Works</span></div></div>
      <h2 class="variety-name">Larkmoor<br>Heritage</h2>
      <p class="variety-style">Dry Cyder</p>
      <div class="style-rule"></div>
      <div class="info-row">
        <div class="info-figures"><span>ALC VOL:<br>6%</span><span class="volume">500ML</span></div>
        <p class="info-pledge">Family craft cider makers using only premium apples from our own traditional Somerset orchard.</p>
        <div class="tree-art" role="img" aria-label="Small apple tree illustration"></div>
      </div>
    </div>
  </section>

  <section class="variety">
    <div class="neck-label"><div class="mark"><span class="mark-dot"></span><span>The Larkmoor Perry Works</span></div></div>
    <div class="body-label label--back">
      <div class="back-head">
        <h2 class="back-title">Larkmoor<br>Heritage</h2>
        <p class="back-address">The Larkmoor Perry Works Ltd.<br>52 Mirefield Row, Taunton, Somerset, TA4 9QX</p>
      </div>
      <div class="back-mark"><div class="mark"><span class="mark-dot"></span><span>The Larkmoor Perry Works</span></div></div>
      <div class="info-row">
        <div class="info-figures"><span>ALC VOL:<br>6%</span><span class="volume">500ML</span></div>
        <p class="info-pledge">Family craft cider makers using only premium apples from our own traditional Somerset orchard.</p>
        <div class="tree-art" role="img" aria-label="Small apple tree illustration"></div>
      </div>
      <p class="batch">Batch number: 1701</p>
      <p class="allergens">Allergens: contains sulphites for freshness</p>
      <div class="story">
        <p>A crisp and refreshing cider, its fresh apple aroma and slightly sweet, ripe apple flavors make it hard to resist.</p>
        <p>Developed to be the perfect balance of sweetness and dry acidity, it's a wonderful blended cider for the seasoned cider geek or a freshman in the subject. It's a gluten free product made completely through the fermentation of apple juice and serves as a testament to the incredible fruit that comes right off the tree on farms across the country, hand selected by the cider makers.</p>
      </div>
      <div class="back-rule"></div>
    </div>
  </section>

  <section class="variety">
    <div class="neck-label"><div class="mark"><span class="mark-dot"></span><span>The Larkmoor Perry Works</span></div></div>
    <div class="body-label label--kingsbury">
      <div class="fruit-art" role="img" aria-label="Faint engraved apple illustration"></div>
      <div class="front-mark"><div class="mark"><span class="mark-dot"></span><span>The Larkmoor Perry Works</span></div></div>
      <h2 class="variety-name">Larkmoor<br>Kingsbury</h2>
      <p class="variety-style">Single Variety Cyder</p>
      <div class="style-rule"></div>
      <div class="info-row">
        <div class="info-figures"><span>ALC VOL:<br>6%</span><span class="volume">500ML</span></div>
        <p class="info-pledge">Family craft cider makers using only premium apples from our own traditional Somerset orchard.</p>
        <div class="tree-art" role="img" aria-label="Small apple tree illustration"></div>
      </div>
    </div>
  </section>

  <section class="variety">
    <div class="neck-label"><div class="mark"><span class="mark-dot"></span><span>The Larkmoor Perry Works</span></div></div>
    <div class="body-label label--amber">
      <div class="fruit-art" role="img" aria-label="Faint engraved apple illustration"></div>
      <div class="front-mark"><div class="mark"><span class="mark-dot"></span><span>The Larkmoor Perry Works</span></div></div>
      <h2 class="variety-name">Larkmoor<br>Amber</h2>
      <p class="variety-style">Medium Dry Cyder</p>
      <div class="style-rule"></div>
      <div class="info-row">
        <div class="info-figures"><span>ALC VOL:<br>6%</span><span class="volume">500ML</span></div>
        <p class="info-pledge">Family craft cider makers using only premium apples from our own traditional Somerset orchard.</p>
        <div class="tree-art" role="img" aria-label="Small apple tree illustration"></div>
      </div>
    </div>
  </section>

</main>
</body>
</html>
```